New audiology website PSD design only - guaranteed

We need a clean and attractive website to replace an existing Audiology (hearing technology) website which will be wordpress based.
The current website is: http://pelmorahearing.com.au
They have a new logo and colors which you can find at www.quodel.net/temp/plh2018.pdf
We will no longer have a web shop in the new website
To enter the competition, we only need a sample of the home page.
The winning design will be asked to produce 2 standard page template alternatives as well (based on the winning home page design, but for a standard page layout)
The winning design must provide any photos used
We want a clean, credible site but with some warmth
Target Market(s)
All ages but needs to include the elderly
Industry/Entity Type
Medical And Science
Number of Pages Required
3 page
Look and feel
Each slider illustrates characteristics of the customer's brand and the style your logo design should communicate.

```html
<!DOCTYPE html>
<html lang="en">
<head>
<meta charset="utf-8">
<title>Pelmora Hearing</title>
<link href="https://fonts.googleapis.com/css2?family=Raleway:wght@400;500;600;700&display=swap" rel="stylesheet">
<style>
:root{
  --orange:#f39a1e;
  --page:#e3e6df;
  --brand-red:#8c2a1c;
  --brand-ring:#e3452a;
  --timing-blue:#2346c8;
  --ink:#333;
  --body:#555;
  --white:#fff;
}
*{margin:0;padding:0;box-sizing:border-box}
html,body{width:1084px;height:1200px;overflow:hidden}
body{background:var(--page);font-family:'Raleway',sans-serif;position:relative}
.top-bar{position:absolute;left:0;top:0;width:1084px;height:13px;background:var(--orange)}
.hero{position:absolute;left:0;top:13px;width:1084px;height:525px;overflow:hidden}
.hero-photo{position:absolute;inset:0;
  background:
    radial-gradient(ellipse 260px 170px at 300px 470px,#ecd274 0%,rgba(236,210,116,0) 100%),
    radial-gradient(ellipse 200px 120px at 520px 300px,#e9cd6c 0%,rgba(233,205,108,0) 100%),
    radial-gradient(ellipse 230px 140px at 230px 260px,#e2c264 0%,rgba(226,194,100,0) 100%),
    radial-gradient(ellipse 140px 300px at 100px 420px,#b88f2e 0%,rgba(184,143,46,0) 100%),
    radial-gradient(ellipse 200px 320px at 420px 440px,#c19835 0%,rgba(193,152,53,0) 100%),
    radial-gradient(ellipse 260px 300px at 780px 230px,#c69c3a 0%,rgba(198,156,58,0) 100%),
    radial-gradient(ellipse 220px 240px at 1000px 60px,#e0bd5c 0%,rgba(224,189,92,0) 100%),
    linear-gradient(110deg,#d8b550 0%,#d2ab46 50%,#c9a03c 75%,#d6b252 100%)}
.brand{position:absolute;left:121px;top:68px;display:flex;align-items:center;gap:14px}
.brand-mark{width:46px;height:46px;border-radius:50%;border:3px solid var(--brand-ring)}
.brand-name{font-size:37px;font-weight:600;color:var(--brand-red);letter-spacing:-.3px}
.call{position:absolute;left:608px;top:63px;width:358px;height:61px;background:rgba(240,205,110,.55);
  display:flex;align-items:center;gap:14px;padding-left:20px;color:var(--white);font-weight:700;font-size:25px}
.nav{position:absolute;left:117px;top:165px;width:850px;height:61px;background:var(--orange);
  border:2px solid #f7b450;border-radius:4px;box-shadow:0 2px 2px rgba(0,0,0,.25);
  display:flex;justify-content:center;align-items:center;gap:16px}
.nav a{color:var(--white);font-weight:700;font-size:17px;text-decoration:none}
.arrow{position:absolute;top:238px}
.timing{position:absolute;left:676px;top:256px;width:291px;height:231px;background:rgba(240,238,228,.85);
  border:2px solid #c8c0a8;border-radius:3px;overflow:hidden}
.timing h2{text-align:center;color:var(--orange);font-size:29px;font-weight:600;margin-top:12px}
.timing-row{position:absolute;left:31px;width:226px;display:flex;justify-content:space-between;
  font-size:12px;color:var(--timing-blue);border-bottom:1px solid var(--timing-blue);height:47px;align-items:center;padding:0 0 0 10px}
.timing-row:nth-of-type(1){top:46px}
.timing-row:nth-of-type(2){top:93px}
.timing-row:nth-of-type(3){top:140px}
.timing-foot{position:absolute;left:0;bottom:0;width:100%;height:13px;background:var(--orange)}
.dots{position:absolute;top:549px;left:512px;display:flex;gap:11px}
.dots span{width:12px;height:12px;border-radius:50%;background:#c9a540}
.dots span:first-child{background:var(--orange)}
.treat{position:absolute;top:640px;left:0;width:1084px;text-align:center}
.treat h2{color:var(--orange);font-size:29px;font-weight:700}
.treat p{width:670px;margin:32px auto 0;font-size:17px;line-height:20.4px;color:var(--body)}
.card{position:absolute;top:944px;width:271px;height:300px;background:var(--white);border:1px solid #d6d6d0}
.card-photo{height:148px}
.card h3{font-size:24px;font-weight:600;color:var(--ink);margin:17px 10px 0}
.card p{font-size:15px;line-height:20.3px;color:var(--body);margin:9px 10px 0;white-space:nowrap}
.photo-wax{background:
  radial-gradient(ellipse 70px 50px at 75px 55px,#c9967a 0%,rgba(201,150,122,0) 100%),
  radial-gradient(ellipse 60px 70px at 230px 90px,#2a1e1a 0%,rgba(42,30,26,0) 100%),
  radial-gradient(ellipse 90px 60px at 160px 40px,#3e5a86 0%,rgba(62,90,134,0) 100%),
  radial-gradient(ellipse 80px 60px at 60px 130px,#2e2c34 0%,rgba(46,44,52,0) 100%),
  linear-gradient(135deg,#4a4e5c,#5e5560 50%,#2a2c34)}
.photo-plugs{background:
  radial-gradient(ellipse 70px 90px at 70px 130px,#241a16 0%,rgba(36,26,22,0) 100%),
  radial-gradient(ellipse 60px 60px at 180px 80px,#c9ada0 0%,rgba(201,173,160,0) 100%),
  radial-gradient(ellipse 60px 40px at 190px 25px,#b4b2b0 0%,rgba(180,178,176,0) 100%),
  radial-gradient(ellipse 70px 50px at 230px 140px,#3a3a40 0%,rgba(58,58,64,0) 100%),
  linear-gradient(90deg,#ece8e4,#f2f0ee)}
.photo-clinic{background:
  radial-gradient(ellipse 45px 60px at 200px 95px,#f2f2ee 0%,rgba(242,242,238,0) 100%),
  radial-gradient(ellipse 60px 30px at 130px 140px,#3c5a8c 0%,rgba(60,90,140,0) 100%),
  radial-gradient(ellipse 30px 40px at 130px 100px,#c9927a 0%,rgba(201,146,122,0) 100%),
  radial-gradient(ellipse 40px 70px at 250px 90px,#e6e8e2 0%,rgba(230,232,226,0) 100%),
  linear-gradient(90deg,#b8a27a,#d8c8a2 35%,#cfc2a2 60%,#9a9a8e)}
</style>
</head>
<body>
<div class="top-bar"></div>
<section class="hero">
  <div class="hero-photo" role="img" aria-label="Audiologist examining a patient's ear with an otoscope, warm gold tint"></div>
  <div class="brand"><span class="brand-mark"></span><span class="brand-name">Pelmora Hearing</span></div>
  <div class="call">
    <svg width="30" height="28" viewBox="0 0 30 28"><path d="M3 10c0-4 5-6 12-6s12 2 12 6v2h-6v-3h-12v3H3z" fill="#e3452a"/><rect x="6" y="13" width="18" height="12" rx="2" fill="#e3452a"/><circle cx="15" cy="19" r="3" fill="#f6d27a"/></svg>
    <span>Call Us: (888) 555 0142</span>
  </div>
  <nav class="nav">
    <a>Your Hearing</a><a>Hearing Aids</a><a>Musicians</a><a>Doctor Information</a><a>About Us</a><a>Products</a><a>Contact Us</a>
  </nav>
  <svg class="arrow" style="left:34px" width="26" height="50" viewBox="0 0 26 50"><path d="M24 2 2 25l22 23" fill="none" stroke="#f39a1e" stroke-width="2"/></svg>
  <svg class="arrow" style="left:1020px" width="26" height="50" viewBox="0 0 26 50"><path d="M2 2l22 23L2 48" fill="none" stroke="#f39a1e" stroke-width="2"/></svg>
  <div class="timing">
    <h2>Our Timing</h2>
    <div class="timing-row"><span>Monday - Friday</span><span>9:00 AM - 6:00PM</span></div>
    <div class="timing-row"><span>Friday - Saturday</span><span>11:00 AM - 6:00PM</span></div>
    <div class="timing-row"><span>Sunday</span><span>Holiday</span></div>
    <div class="timing-foot"></div>
  </div>
</section>
<div class="dots"><span></span><span></span><span></span></div>
<section class="treat">
  <h2>What We Treat</h2>
  <p>Pelmora Hearing is a leading Hearing and Balance Clinic located in the inner suburbs of Sydney. Each of our custom built clinics have the most up to date diagnostic equipment available. We offer an extensive range of diagnostics conducted by highly experienced and fully trained Audiologists. We work closely with medical professionals to deliver outstanding and reliable services.medical professionals to deliver outstanding and reliable services.</p>
</section>
<article class="card" style="left:119px">
  <div class="card-photo photo-wax" role="img" aria-label="Clinician checking a patient's ear with a small light"></div>
  <h3>Ear Wax Build Up</h3>
  <p>Wax Build Up Can Lead To<br>Temporary Hearing Loss &amp; Be Very<br>Uncomfortable. We Use Ear</p>
</article>
<article class="card" style="left:407px">
  <div class="card-photo photo-plugs" role="img" aria-label="Older man holding his hand to his ear beside a woman"></div>
  <h3>Ear Plugs</h3>
  <p>Working In Noisy Environments<br>Or Taking Part In Leisure<br>Activities Such As Shooting,</p>
</article>
<article class="card" style="left:695px">
  <div class="card-photo photo-clinic" role="img" aria-label="Doctor fitting a hearing test device on a patient in a clinic room"></div>
  <h3>Hearing Protction</h3>
  <p>Hearing Loss Happens Over Time<br>And Is Virtually Unnoticeable<br>Until It Starts To Disrupt Your</p>
</article>
</body>
</html>
```